Contemporary Business card for Event Manager

Needed for my startup events company in Melbourne. Events I manage will be based within the fashion industry, sporting events, product launches etc. Not weddings or small dinner parties. Therfore I am after something professional and aimed at high end corporate market; but with the added emphasis on not being too conservative or boring. I am happy with a pop of colour e.g. yellow or copper foil.

Target Market(s)

fashion industry, design industry, high end sporting events e.g. Polo, Grand Prix, corporate clients,

Industry/Entity Type

Fashion

Contact Information for Business Card

side 1
Lena Varsby (can be upper or lower case, have a feature full stop between first and surname, or at the end of the nameetc) I am open to ideas. I would also be fine with my initials or name as a logo on the front (if this is the case my full name would need to go on the second side of the card.
2nd side:
Mobile: +61 491 570 156
email: lena.varsby@mailtrove.com.au

on one side of the card:
event management | brand activation | Advisory Services

Font styles to use
Serif
Sans Serif

Requirements
Must have
• side 2 must have
• mobile number
• email address
• event management | brand activation | Advisory Services
• ** my full name (Lena Varsby) must be on the card somewhere)
Nice to have
• 1st side
• I see the card stock being either a dark grey, light grey, natural white or black (all matt colours on unprocessed card). I see the writing being copper foil, or foil white or foil black.
• To give you a feel for me, think: contemporary, minimalist, I love line drawings, concrete, white with grey vein marble, copper, white, grey, black...yes I do like colour....yellow (but pops of colour) ;) I would like the card to look designer but 'on trend' as I deal with a lot of design and fashion clients....styles - think the sophistication and simplicity of Morvane or urban contemporary.
• some examples of what I like. Although please don't leet this limit you...I really am happy to have something a little more urban or design focused like a line drawing of an object, person too or a photo image too.
• https://www.moodfolia.com/pin/100000000000000001/
• https://www.moodfolia.com/pin/100000000000000002/
• https://www.moodfolia.com/pin/100000000000000003/
• https://www.moodfolia.com/pin/10000000000000004/
• https://www.moodfolia.com/pin/10000000000000005/
• https://www.moodfolia.com/pin/10000000000000006/
• https://www.moodfolia.com/pin/100000000000000007/
• https://www.moodfolia.com/pin/100000000000000008/
• https://www.moodfolia.com/pin/100000000000000009/
Should not have
• should not look commercial or have cartoonish looking logos. However happy with a simple line drawing or logo with initials etc.

```html
<!DOCTYPE html>
<html lang="en">
<head>
<meta charset="utf-8">
<title>Lena Varsby – Business Card</title>
<link href="https://fonts.googleapis.com/css2?family=Tinos:wght@400;700&display=swap" rel="stylesheet">
<style>
  :root {
    --page-bg: #ece9e3;
    --gold-light: #f6e27a;
    --gold-mid: #e8c73a;
    --gold-deep: #d4a819;
    --card-white: #fbfbfa;
    --ink-dark: #3a3a3a;
    --ink-grey: #6f6f6f;
    --card-edge: #d9d6cf;
  }
  html, body {
    margin: 0;
    padding: 0;
    width: 1200px;
    height: 818px;
    overflow: hidden;
    background: var(--page-bg);
    font-family: "Tinos", "Times New Roman", serif;
  }
  .canvas {
    position: relative;
    width: 1200px;
    height: 818px;
  }
  .business-card {
    position: absolute;
    left: 150px;
    top: 151px;
    width: 900px;
    height: 515px;
    box-shadow: 0 10px 30px rgba(0,0,0,0.18);
    outline: 1px solid var(--card-edge);
  }
  .card-artwork {
    position: absolute;
    inset: 0;
    width: 900px;
    height: 515px;
    display: block;
  }
  .services {
    position: absolute;
    right: 150px;
    top: 46px;
    margin: 0;
    padding: 0;
    list-style: none;
    font-weight: 700;
    font-size: 27px;
    line-height: 34px;
    color: var(--ink-dark);
  }
  .services li:nth-child(2) { padding-left: 26px; }
  .services li:nth-child(3) { padding-left: 52px; }
  .identity {
    position: absolute;
    left: 150px;
    top: 226px;
  }
  .full-name {
    margin: 0;
    font-weight: 400;
    font-size: 70px;
    line-height: 1;
    color: var(--ink-grey);
    letter-spacing: 1px;
    text-shadow: 0 1px 0 #ffffff, 0 -1px 1px rgba(0,0,0,0.15);
  }
  .contact-list {
    margin: 26px 0 0 88px;
    padding: 0;
    list-style: none;
    font-size: 32px;
    line-height: 44px;
    color: var(--ink-dark);
  }
  .contact-list li {
    display: flex;
    align-items: center;
    gap: 14px;
  }
  .contact-icon {
    width: 24px;
    height: 24px;
    flex: none;
  }
</style>
</head>
<body>
<main class="canvas">
  <section class="business-card">
    <svg class="card-artwork" viewBox="0 0 900 515" xmlns="http://www.w3.org/2000/svg" aria-hidden="true">
      <defs>
        <linearGradient id="goldFoil" x1="0" y1="0" x2="1" y2="1">
          <stop offset="0" stop-color="var(--gold-deep)"/>
          <stop offset="0.35" stop-color="var(--gold-light)"/>
          <stop offset="0.65" stop-color="var(--gold-mid)"/>
          <stop offset="1" stop-color="var(--gold-light)"/>
        </linearGradient>
      </defs>
      <rect class="gold-ground" width="900" height="515" fill="url(#goldFoil)"/>
      <path class="white-lens" d="M 60 515 C 40 300 120 60 330 0 L 900 0 L 900 60 C 760 250 620 470 520 515 Z" fill="var(--card-white)"/>
      <path class="white-lens-top" d="M 330 0 C 520 -10 700 0 900 0 L 900 20 C 860 10 700 5 330 0 Z" fill="var(--card-white)"/>
    </svg>

    <ul class="services">
      <li>Event management</li>
      <li>Brand activation</li>
      <li>Advisory Services</li>
    </ul>

    <div class="identity">
      <h1 class="full-name">Lena Varsby</h1>
      <ul class="contact-list">
        <li>
          <svg class="contact-icon" viewBox="0 0 24 24" aria-label="Mobile">
            <path d="M7 2 C5 3 3 6 4 10 C6 16 10 20 15 21 C18 22 20 20 21 18 L17 14 L14 16 C11 14 10 13 8 10 L10 7 Z" fill="var(--ink-dark)"/>
          </svg>
          <span>+61 491 570 156</span>
        </li>
        <li>
          <svg class="contact-icon" viewBox="0 0 24 24" aria-label="Email">
            <rect x="2" y="5" width="20" height="14" fill="var(--ink-dark)"/>
            <path d="M2 5 L12 13 L22 5 M2 19 L9 11 M22 19 L15 11" stroke="var(--card-white)" stroke-width="1.4" fill="none"/>
          </svg>
          <span>lena.varsby@mailtrove.com.au</span>
        </li>
      </ul>
    </div>
  </section>
</main>
</body>
</html>
```